Homepage design for female-owned English/French speaking Law firm

Brief Update - we prefer not to have a photo of a person in the hero shot

Morlewy.com.au is the website for a English/French Bilingual Female-owned Law Firm, Quillomette Morlewy.
Overall Design notes:
Professional, yet warm and welcoming
Historic foundations but Progressive, woman-owned, sleek, innovative and modern.
Approachable, casual yet professional. Sans-serif font and light colours would help this
2 languages switched by flags (English/French)

Winner must provide
Home page design
Standard (inner) page design (can be provided after winner is selected)
All photos used in the design without charge

Number of Pages Required

2 page

Requirements
Should not have
• Update - we prefer not to have a photo of a person in the hero shot

```html
<!DOCTYPE html>
<html lang="en">
<head>
<meta charset="utf-8">
<title>Quillomette Morlewy</title>
<link rel="stylesheet" href="https://fonts.googleapis.com/css2?family=Playfair+Display:wght@700&family=Poppins:wght@400;500;600&family=Roboto:wght@400;500;700&family=Arimo:wght@400&display=swap">
<style>
:root{
  --orange:#fd8b25;
  --ink:#333333;
  --body:#6b6b6b;
  --muted:#9a9a9a;
  --cream:#f4f0ed;
  --line:#d9d9d9;
  --footer:#4a4a4a;
  --white:#ffffff;
}
*{box-sizing:border-box;margin:0;padding:0}
html,body{width:1200px;height:3110px;overflow:hidden;background:var(--white)}
body{position:relative;font-family:"Poppins",sans-serif;color:var(--body)}
.abs{position:absolute}
.serif{font-family:"Playfair Display",serif;color:var(--ink);font-weight:700;line-height:1}
.btn{position:absolute;background:var(--orange);color:var(--white);font-family:"Roboto",sans-serif;font-weight:500;border-radius:20px;display:flex;align-items:center;justify-content:center;text-transform:uppercase}
.top-rule{top:0;left:0;width:1200px;height:3px;background:var(--orange)}
.brand{left:160px;top:28px;display:flex;align-items:center;gap:9px;font-family:"Poppins",sans-serif;font-size:19px;font-weight:500;color:var(--ink)}
.brand-mark{width:12px;height:12px;background:var(--orange)}
.nav{top:36px;right:160px;display:flex;font-size:11px;font-family:"Poppins",sans-serif}
.nav a{color:var(--muted);text-decoration:none;margin-left:30px}
.nav a.active{color:var(--orange);font-weight:500}
.hero{top:78px;left:0;width:1200px;height:444px;background:var(--cream)}
.hero-kicker{left:159px;top:183px;font-size:22px}
.hero-title{left:159px;top:208px;font-size:46px;letter-spacing:.5px}
.hero-text{left:158px;top:269px;width:345px;font-family:"Arimo",sans-serif;font-size:12.5px;line-height:19px;color:var(--body)}
.hero-art{left:580px;top:104px;width:535px;height:382px;border-radius:8px;background:radial-gradient(circle at 60% 55%,#c89a72 0%,#e6d6c8 45%,var(--cream) 75%)}
.about-back{left:143px;top:755px;width:235px;height:258px;background:var(--orange);border-radius:18px}
.about-img{left:160px;top:612px;width:390px;height:388px;border-radius:14px;background:linear-gradient(135deg,#e8e4e2 0%,#cdc4bd 45%,#8b6a4c 75%,#5a3c2a 100%);box-shadow:0 4px 14px rgba(0,0,0,.12)}
.h2{font-size:34px;letter-spacing:.3px}
.about-title{left:605px;top:630px}
.about-text{left:605px;top:678px;width:435px;font-size:12px;line-height:19px;text-align:justify}
.checks{left:605px;top:850px;list-style:none;font-size:12px;font-weight:600;color:#555}
.checks li{display:flex;align-items:center;gap:9px;height:22.5px}
.feature{top:1076px;width:260px}
.feature>svg{display:block;margin-bottom:22px}
.feature h3{font-family:"Playfair Display",serif;font-weight:400;font-size:12px;color:var(--ink);letter-spacing:.2px;text-transform:uppercase}
.feature p{font-size:11.5px;line-height:16px;margin-top:9px;width:252px}
.link-more{font-family:"Roboto",sans-serif;font-size:11.5px;color:var(--orange);font-weight:500;display:flex;align-items:center;gap:8px;margin-top:17px}
.practice-bg{left:0;top:1318px;width:1200px;height:512px;background:linear-gradient(180deg,#ffffff 0%,#eeeeee 30%,#ececec 80%,#ffffff 100%)}
.kicker{font-family:"Roboto",sans-serif;font-weight:500;font-size:15px;color:var(--orange);text-align:center;width:1200px;left:0}
.center-title{left:0;width:1200px;text-align:center}
.card-img{top:1475px;width:279px;height:210px;border-radius:12px;box-shadow:0 4px 10px rgba(0,0,0,.15)}
.card-cap{top:1697px;font-family:"Playfair Display",serif;font-size:15px;color:var(--ink)}
.card-link{top:1726px;font-size:11px;color:#f4a25a}
.stats-shadow{left:152px;top:1795px;width:262px;height:91px;background:#5e5e5e}
.stats{left:160px;top:1774px;width:878px;height:102px;background:var(--white);box-shadow:0 2px 10px rgba(0,0,0,.12);display:flex;align-items:center}
.stat{padding-left:34px;height:56px;border-right:1px solid var(--line)}
.stat b{display:block;font-family:"Roboto",sans-serif;font-weight:500;font-size:36px;color:var(--ink);line-height:38px}
.stat span{font-size:11.5px;color:var(--muted);white-space:nowrap}
.view-more{left:888px;top:1788px;width:137px;height:88px;background:var(--orange);color:var(--white);font-family:"Roboto",sans-serif;font-weight:500;font-size:19px;display:flex;align-items:center;justify-content:center}
.hist-kicker{left:160px;top:2016px;font-family:"Roboto",sans-serif;font-weight:500;font-size:15px;color:var(--orange)}
.hist-title{left:160px;top:2038px}
.hist-text{left:160px;top:2090px;width:508px;font-size:11.5px;line-height:16px;text-align:justify}
.hist-text p{margin-bottom:15px}
.hist-back{left:940px;top:2022px;width:98px;height:293px;background:linear-gradient(135deg,#f3a04f,var(--orange));border-radius:0 0 34px 0}
.hist-img{left:717px;top:2000px;width:253px;height:337px;background:linear-gradient(180deg,#8f949b 0%,#c7c5c1 45%,#c89660 70%,#7a4f2f 100%)}
.contact-card{left:160px;top:2518px;width:315px;height:324px;background:var(--orange);border-radius:0 50px 0 50px;color:var(--white);font-family:"Roboto",sans-serif}
.ci{position:absolute;left:26px;display:flex;gap:14px}
.ci h4{font-size:15px;font-weight:500;letter-spacing:.2px}
.ci p{font-size:11.5px;font-weight:700;line-height:17px;margin-top:3px;padding-left:2px}
.ci svg{flex:none;width:18px;margin-top:1px}
.form-intro{left:515px;top:2522px;width:525px;font-size:13px;line-height:17px;color:var(--muted)}
.lbl{font-size:10.5px;color:var(--muted)}
.field{border:1px solid var(--line);background:var(--white)}
.footer{left:0;top:2928px;width:1200px;height:132px;background:var(--footer)}
.social{top:2951px;width:38px;height:38px;border:1.5px solid var(--white);border-radius:50%}
.foot-nav{top:3013px;left:0;width:1200px;display:flex;justify-content:center;font-family:"Roboto",sans-serif;font-weight:700;font-size:11px;color:var(--white)}
.foot-nav span{margin:0 20px}
.foot-nav .active{color:var(--orange)}
.copy{left:0;top:3060px;width:1200px;height:50px;background:var(--orange);color:var(--white);font-family:"Roboto",sans-serif;font-size:10px;display:flex;align-items:center;justify-content:center}
</style>
</head>
<body>

<div class="abs top-rule"></div>
<header>
  <div class="abs brand"><span class="brand-mark"></span>Quillomette Morlewy</div>
  <nav class="abs nav">
    <a class="active">Home</a><a>Our Services</a><a style="margin-left:40px">Download</a><a>Contact us</a><a style="margin-left:20px">Links</a>
  </nav>
</header>

<section class="abs hero"></section>
<div class="abs serif hero-kicker">OUR SMALL,</div>
<h1 class="abs serif hero-title">SKILLED TEAM</h1>
<p class="abs hero-text">Lorem ipsum dolor sit amet, consectetur adipiscing elit. Sed tincidunt nisi a turpis interdum consequat. Pellentesque ut semper ex. Morbi mauris ipsum, efficitur .</p>
<div class="btn" style="left:160px;top:360px;width:141px;height:40px;font-size:13px">Contact us</div>
<div class="abs hero-art" role="img" aria-label="Illustration of scales of justice, stacked law books, a lawyer holding papers, a plant and a quill in an inkpot"></div>

<div class="abs about-back"></div>
<div class="abs about-img" role="img" aria-label="Photo of a bronze Lady Justice statue with a gavel"></div>
<h2 class="abs serif h2 about-title">ABOUT MORLEWY</h2>
<div class="abs about-text">
  <p>Our small, skilled team is committed to the delivery of quality legal services to our clients.</p>
  <p>Quillomette Morlewy originated with the legal practice founded by Mr Lucien Armand Quillomette in the 1930s. Today, we are a progressive law firm that has embraced both the traditional approach of our predecessor firms and the efficiencies of modern technology.</p>
  <p>All of our services are available in English or in French according to the needs of our clients.</p>
</div>
<ul class="abs checks">
  <li><svg width="13" height="13" viewBox="0 0 13 13"><rect x="1" y="2" width="10" height="10" rx="1.5" fill="none" stroke="#fd8b25" stroke-width="1.4"/><path d="M3.5 6.5l2.5 2.5 6-7" fill="none" stroke="#fd8b25" stroke-width="1.6"/></svg>Mission statement.</li>
  <li><svg width="13" height="13" viewBox="0 0 13 13"><rect x="1" y="2" width="10" height="10" rx="1.5" fill="none" stroke="#fd8b25" stroke-width="1.4"/><path d="M3.5 6.5l2.5 2.5 6-7" fill="none" stroke="#fd8b25" stroke-width="1.6"/></svg>Claire Morlewy.</li>
  <li><svg width="13" height="13" viewBox="0 0 13 13"><rect x="1" y="2" width="10" height="10" rx="1.5" fill="none" stroke="#fd8b25" stroke-width="1.4"/><path d="M3.5 6.5l2.5 2.5 6-7" fill="none" stroke="#fd8b25" stroke-width="1.6"/></svg>History.</li>
  <li><svg width="13" height="13" viewBox="0 0 13 13"><rect x="1" y="2" width="10" height="10" rx="1.5" fill="none" stroke="#fd8b25" stroke-width="1.4"/><path d="M3.5 6.5l2.5 2.5 6-7" fill="none" stroke="#fd8b25" stroke-width="1.6"/></svg>Location.</li>
</ul>
<div class="btn" style="left:608px;top:958px;width:114px;height:32px;font-size:13px">Read more</div>

<div class="abs feature" style="left:160px">
  <svg width="50" height="46" viewBox="0 0 50 46" fill="none" stroke="#7a5a45" stroke-width="1.6"><path d="M3 14L25 3l22 11z"/><path d="M5 16h40M5 40h40M2 44h46"/><path d="M10 18v20M17 18v20M25 18v20M33 18v20M40 18v20"/></svg>
  <h3>Winning award law firm</h3>
  <p>Lawyers and attorneys act as both legal advisors and advocates, guiding individuals and businesses through intricate legal processes.</p>
  <div class="link-more">READ MORE <svg width="13" height="7" viewBox="0 0 13 7"><path d="M0 3.5h11M8 1l3 2.5L8 6" stroke="#fd8b25" stroke-width="1.5" fill="none"/></svg></div>
</div>
<div class="abs feature" style="left:476px">
  <svg width="50" height="46" viewBox="0 0 50 46" fill="none" stroke="#7a5a45" stroke-width="1.6"><path d="M3 2h26l6 6v36H3z"/><path d="M8 12h16M8 18h16M8 24h12M8 30h10"/><path d="M22 40l18-18 4 4-18 18h-4z"/></svg>
  <h3>Confidential</h3>
  <p>Lawyers and attorneys act as both legal advisors and advocates, guiding individuals and businesses through intricate legal processes.</p>
  <div class="link-more">READ MORE <svg width="13" height="7" viewBox="0 0 13 7"><path d="M0 3.5h11M8 1l3 2.5L8 6" stroke="#fd8b25" stroke-width="1.5" fill="none"/></svg></div>
</div>
<div class="abs feature" style="left:792px">
  <svg width="50" height="46" viewBox="0 0 50 46" fill="none" stroke="#7a5a45" stroke-width="1.6"><path d="M25 2v40M15 44h20M6 9h38"/><path d="M10 9L3 26h14zM40 9l-7 17h14z"/><path d="M3 26a7 4 0 0 0 14 0M33 26a7 4 0 0 0 14 0"/></svg>
  <h3>Legal protection</h3>
  <p>Lawyers and attorneys act as both legal advisors and advocates, guiding individuals and businesses through intricate legal processes.</p>
  <div class="link-more">READ MORE <svg width="13" height="7" viewBox="0 0 13 7"><path d="M0 3.5h11M8 1l3 2.5L8 6" stroke="#fd8b25" stroke-width="1.5" fill="none"/></svg></div>
</div>

<div class="abs practice-bg" role="img" aria-label="Faint background photo of a Lady Justice statue holding scales"></div>
<div class="abs kicker" style="top:1372px">OUR EXPERTISE</div>
<h2 class="abs serif center-title" style="top:1396px;font-size:35px">LEGAL PRACTICE AREAS</h2>

<div class="abs card-img" style="left:160px;background:linear-gradient(135deg,#cfd3d6,#8c9297 55%,#3d4347)" role="img" aria-label="Photo of a person signing documents beside a laptop and a building model"></div>
<div class="abs card-img" style="left:460px;background:linear-gradient(135deg,#f2f0ed,#d6c6b6 45%,#8a5a36 80%,#3b2a22)" role="img" aria-label="Photo of house keys on a wooden desk beside a gavel"></div>
<div class="abs card-img" style="left:760px;background:linear-gradient(135deg,#2a9fb8,#1b8aa5 60%,#167b93)" role="img" aria-label="Illustration of a lawyer, a gavel, law books and a coin"></div>
<div class="abs card-cap" style="left:160px">Property law</div>
<div class="abs card-cap" style="left:463px">Sale of Business</div>
<div class="abs card-cap" style="left:760px">Elder Law</div>
<div class="abs link-more card-link" style="left:160px;margin:0">READ MORE <svg width="13" height="7" viewBox="0 0 13 7"><path d="M0 3.5h11M8 1l3 2.5L8 6" stroke="#fd8b25" stroke-width="1.5" fill="none"/></svg></div>
<div class="abs link-more card-link" style="left:460px;margin:0">READ MORE <svg width="13" height="7" viewBox="0 0 13 7"><path d="M0 3.5h11M8 1l3 2.5L8 6" stroke="#fd8b25" stroke-width="1.5" fill="none"/></svg></div>
<div class="abs link-more card-link" style="left:760px;margin:0">READ MORE <svg width="13" height="7" viewBox="0 0 13 7"><path d="M0 3.5h11M8 1l3 2.5L8 6" stroke="#fd8b25" stroke-width="1.5" fill="none"/></svg></div>

<div class="abs stats-shadow"></div>
<div class="abs stats">
  <div class="stat" style="width:176px"><b>1000+</b><span>Client Consultations</span></div>
  <div class="stat" style="width:160px;padding-left:32px"><b>95%</b><span>Successful Cases</span></div>
  <div class="stat" style="width:204px;padding-left:30px"><b>10m</b><span>Recovered cost for clients</span></div>
  <div class="stat" style="width:185px;border:none;padding-left:30px"><b>30+</b><span>Professional Attorneys</span></div>
</div>
<div class="abs view-more">VIEW MORE</div>

<div class="abs hist-kicker">HISTORY</div>
<h2 class="abs serif h2 hist-title">QUILLOMETTE MORLEWY</h2>
<div class="abs hist-text">
  <p>Quillomette Morlewy is a successor to the legal practice founded by Mr Lucien Armand Quillomette in the 1930?s. Its various transformations saw Mr Lucien Armand Quillomette and his sons work in partnership with other lawyers prior to forming a smaller family firm (Quillomette &amp; Quillomette) on their own.</p>
  <p>The firm name was changed to ?Quillomette? when Peter Quillomette became sole proprietor of the firm in the early 1990?s.</p>
  <p>After working as an employed Solicitor with Peter Quillomette, Claire Morlewy became proprietor of the firm in 1996 and the name of the practice was changed to ?Quillomette Morlewy?.</p>
</div>
<div class="btn" style="left:161px;top:2284px;width:114px;height:32px;font-size:13px">Read more</div>
<div class="abs hist-back"></div>
<div class="abs hist-img" role="img" aria-label="Photo of a wooden house model beside a gavel"></div>

<div class="abs kicker" style="top:2413px">GET IN TOUCH</div>
<h2 class="abs serif center-title" style="top:2434px;font-size:35px">CONTACT US</h2>

<div class="abs contact-card">
  <div class="ci" style="top:52px"><svg viewBox="0 0 18 22" height="20"><path d="M9 1a7 7 0 0 0-7 7c0 5 7 13 7 13s7-8 7-13a7 7 0 0 0-7-7z" fill="#fff"/><circle cx="9" cy="8" r="2.6" fill="#fd8b25"/></svg><div><h4>ADDRESS</h4><p>Level 9, 48 Harbourview Street Sydney, NSW<br>2000</p></div></div>
  <div class="ci" style="top:135px"><svg viewBox="0 0 20 20" height="18"><path d="M4 1l4 4-2 3c1 3 3 5 6 6l3-2 4 4-3 3C8 19 1 12 1 4z" fill="#fff"/></svg><div><h4>PHONE</h4><p>(+612) 9000 1234</p></div></div>
  <div class="ci" style="top:198px;left:20px"><svg viewBox="0 0 26 22" width="26" height="22" fill="none" stroke="#fff" stroke-width="1.5"><rect x="6" y="1" width="14" height="7"/><rect x="1" y="8" width="24" height="10" rx="2"/><rect x="6" y="14" width="14" height="7"/></svg><div style="margin-left:-4px"><h4>FAX</h4><p>(+612) 9000 5678</p></div></div>
  <div class="ci" style="top:258px"><svg viewBox="0 0 20 14" height="14"><rect width="20" height="14" rx="1.5" fill="#fff"/><path d="M1 1l9 7 9-7" stroke="#fd8b25" stroke-width="1.5" fill="none"/></svg><div><h4>EMAIL</h4><p>claire@morlewy.com.au</p></div></div>
</div>

<p class="abs form-intro">Lorem ipsum dolor sit amet, consectetur adipiscing elit. Sed tincidunt nisi a turpis interdum consequat. Pellentesque ut semper</p>
<div class="abs lbl" style="left:516px;top:2574px">Name</div>
<div class="abs lbl" style="left:782px;top:2574px">EMail</div>
<div class="abs field" style="left:515px;top:2594px;width:259px;height:36px"></div>
<div class="abs field" style="left:781px;top:2594px;width:259px;height:36px"></div>
<div class="abs lbl" style="left:516px;top:2643px">Phone</div>
<div class="abs field" style="left:515px;top:2662px;width:525px;height:36px"></div>
<div class="abs lbl" style="left:516px;top:2712px">Message</div>
<div class="abs field" style="left:515px;top:2732px;width:525px;height:60px"></div>
<div class="btn" style="left:516px;top:2818px;width:127px;height:32px;font-size:13px">Submit</div>

<footer>
  <div class="abs footer"></div>
  <div class="abs social" style="left:512px" role="img" aria-label="Social link"></div>
  <div class="abs social" style="left:557px" role="img" aria-label="Social link"></div>
  <div class="abs social" style="left:603px" role="img" aria-label="Social link"></div>
  <div class="abs social" style="left:650px" role="img" aria-label="Social link"></div>
  <div class="abs foot-nav"><span class="active">HOME</span><span>OUR SERVICES</span><span>DOWNLOAD</span><span>CONTACT US</span><span>LINKS</span></div>
  <div class="abs copy">© 2024 QUILLOMETTE MORLEWY | ALL RIGHT RESERVED.</div>
</footer>

</body>
</html>
```